Talvern Asset Management - Corporate Letter Head Project

Looking for a classy design based on our current logo. Please find current logo source file in files. With our color scheme.

Target Market(s)

We're an investment firm, the letterhead needs to look professional and attractive to clients.

Industry/Entity Type

Hedgefund

Colors
0054AA
0677BA
7BADD7
CADEEF
E8F1F8

Requirements
Must have
• Our logo, address, phone number, and email

```html
<!DOCTYPE html>
<html lang="en">
<head>
<meta charset="utf-8">
<title>Talvern Asset Management – Letterhead</title>
<link rel="stylesheet" href="https://fonts.googleapis.com/css2?family=Arimo:wght@400;700&display=swap">
<style>
  :root {
    --page: #e9e9eb;
    --ink: #484848;
    --brand-navy: #1c2a3c;
    --signature-tone: #c9cacd;
  }
  html, body {
    margin: 0;
    padding: 0;
    width: 950px;
    height: 1200px;
    overflow: hidden;
    background: var(--page);
  }
  .letterhead {
    position: relative;
    width: 950px;
    height: 1200px;
    background: var(--page);
    font-family: "Arimo", Helvetica, Arial, sans-serif;
    color: var(--ink);
  }
  .brand {
    position: absolute;
    top: 78px;
    left: 0;
    width: 950px;
    display: flex;
    flex-direction: column;
    align-items: center;
    gap: 18px;
  }
  .brand-square {
    width: 52px;
    height: 52px;
    border: 1.5px solid var(--brand-navy);
    box-sizing: border-box;
  }
  .brand-name {
    margin: 0;
    font-size: 19px;
    font-weight: 400;
    letter-spacing: 0.06em;
    text-transform: uppercase;
    color: var(--brand-navy);
  }
  .recipient {
    position: absolute;
    top: 349px;
    left: 82px;
    margin: 0;
    font-style: normal;
    font-size: 14px;
    line-height: 16px;
  }
  .salutation {
    position: absolute;
    top: 474px;
    left: 84px;
    margin: 0;
    font-size: 15px;
    font-weight: 700;
  }
  .letter-body {
    position: absolute;
    top: 536px;
    left: 84px;
    width: 790px;
  }
  .letter-body p {
    margin: 0 0 16px;
    font-size: 14.2px;
    line-height: 16px;
  }
  .sender {
    position: absolute;
    top: 862px;
    left: 88px;
  }
  .sender-name {
    margin: 0;
    font-size: 17px;
    font-weight: 700;
    line-height: 22px;
  }
  .sender-title {
    margin: 0;
    font-size: 17px;
    line-height: 22px;
  }
  .signature {
    position: absolute;
    top: 925px;
    left: 82px;
    width: 150px;
    height: 66px;
    background: linear-gradient(90deg, var(--signature-tone), var(--page));
    border-radius: 4px;
  }
  .contact-footer {
    position: absolute;
    top: 1126px;
    left: 0;
    width: 950px;
    display: flex;
    justify-content: center;
    align-items: center;
    gap: 22px;
    font-size: 13.5px;
  }
  .contact-item {
    display: flex;
    align-items: center;
    gap: 8px;
  }
  .contact-item svg {
    fill: var(--brand-navy);
  }
</style>
</head>
<body>
<main class="letterhead">
  <header class="brand">
    <div class="brand-square"></div>
    <h1 class="brand-name">Talvern Asset Management</h1>
  </header>

  <address class="recipient">
    Mr Daniel Ashford<br>
    Founder and CEO<br>
    Your Company,<br>
    4412 Cedarline Avenue, Suite 2200<br>
    Kingsport, Canada 48120
  </address>

  <p class="salutation">Dear Sir</p>

  <section class="letter-body">
    <p>Lorem ipsum dolor sit amet. Non quam iste ut dolor repellendus aut quasi porro nam molestias ullam ut sint ipsa! Qui accusamus assumenda qui quae tempore sit quia velit aut porro tempora. Est iste explicabo aut alias impedit est sequi quis.</p>
    <p>Cum rerum molestiae id galisum odit et autem voluptas aut blanditiis iste ut aspernatur itaque ut tempora laudantium vel voluptatem repudiandae! Ea delectus omnis est voluptas odit ut assumenda quisquam eos facere sunt qui quis vitae. Qui velit dolorem in distinctio</p>
    <p>dignissimos rem voluptatem totam ut quia nostrum cum quas consequuntur. Quo aliquid earum eum optio ducimus qui fugiat veniam qui blanditiis velit ut quos dolores non officiis enim ut voluptatem veritatis.</p>
    <p>At quia sunt nam quibusdam mollitia aut rerum laudantium et inventore molestiae aut cumque consequatur. 33 minima velit rem quasi galisum ut quae magni sed praesentium possimus 33 commodi quam qui quae aperiam est enim accusantium. Sed Quis laboriosam ut suscipit maxime cum reprehenderit adipisci. Non nihil dolor ut obcaecati commodi aut Quis provident eos doloribus cumque.</p>
    <p>At quia sunt nam quibusdam mollitia aut rerum laudantium et inventore molestiae aut cumque consequatur. 33 minima velit rem quasi galisum ut quae</p>
  </section>

  <section class="sender">
    <p class="sender-name">PETER LINDQVIST</p>
    <p class="sender-title">President</p>
  </section>

  <div class="signature" role="img" aria-label="Handwritten signature of the president"></div>

  <footer class="contact-footer">
    <span class="contact-item">4412 Cedarline Avenue, Kingsport, Canada 48120</span>
    <span class="contact-item">
      <svg width="10" height="11" viewBox="0 0 24 24" aria-hidden="true"><path d="M6.6 10.8a15.1 15.1 0 0 0 6.6 6.6l2.2-2.2c.3-.3.7-.4 1-.2 1.1.4 2.3.6 3.6.6.6 0 1 .4 1 1V20c0 .6-.4 1-1 1A17 17 0 0 1 3 4c0-.6.4-1 1-1h3.5c.6 0 1 .4 1 1 0 1.3.2 2.5.6 3.6.1.3 0 .7-.2 1l-2.3 2.2z"/></svg>
      555-214-0198
    </span>
    <span class="contact-item">
      <svg width="10" height="8" viewBox="0 0 20 16" aria-hidden="true"><path d="M0 0h20v16H0z M2 2v1l8 5 8-5V2z" fill-rule="evenodd"/></svg>
      info@talvernasset.com
    </span>
  </footer>
</main>
</body>
</html>
```